Copperleaf Dukes - Sovereign rings, pendants & custom cultural pieces

I need a website that attracts customers knowing that I am as per detailed below Everyone deserves a special piece of treasure. At Copperleaf Dukes we provide you with unique, high-quality and affordable Sovereign rings, pendants & custom cultural pieces.
Feel free to check my Snapgallery page to get idea's @copperleaf.dukes
I want people to see the Items I have available & know that my prices are very competitive. I want people to be able to Shop/Purchase items via site. I would like to have Copperleaf Dukes Chatterbook, Snapgallery & Swapyard Icon/tabs on site so customers can link a at click of the mouse.

(My Apologies to you all, This is all overwhelming & new to myself & I appreciate your efforts & work detail)
Updates

Apologies, have had family loss to deal with

Still dealing with loss of family member

Still Dealing with Family member passing

As previously, still getting through the loss of a family member

As per previous extensions, re adjusting to life after loss of family member

As per previously still recovering from loss of family member

As previously expressed

Haven’t recovered from family loss

I am still getting life back together

Target Market(s)

Jewellery, Wedding, Gifts, Pacific people, Persons 18 - 65yrs, New Zealand & Australian

Industry/Entity Type

Jewelry

Contact Information for Business Card

Copperleaf Dukes
Rek Tamuno
Chatterbook @copperleafdukes
Snapgallery @copperleaf.dukes
Phone Number 021 04731952
Website www.copperleafdukes.co.nz
Auckland
New Zealand

Number of Pages Required

5+ page

Font styles to use
Sans Serif

Colors
474747
1b1b1b
000000
cfcfcf
fbed22
ffc214
ffffff

Requirements
Must have
• Using Black / Gold Copperleaf Dukes logo with crown, has been attached to Web design.
• Rek Tamuno
• Chatterbook Copperleaf Dukes
• Snapgallery @copperleaf.dukes
• Swapyard Copperleaf Dukes
• Phone Number 021 04731952
• Website www.copperleafdukes.co.nz
Nice to have
• Thinking black card with the Copperleaf Dukes Gold logo
• Lines on back of card for Customer Quoted Prices

```html
<!DOCTYPE html>
<html lang="en">
<head>
<meta charset="utf-8">
<title>Copperleaf Dukes — Business Card</title>
<link href="https://fonts.googleapis.com/css2?family=Lato:wght@400;700&display=swap" rel="stylesheet">
<style>
  :root {
    --ink: #1b1b1b;
    --black: #000000;
    --gold: #6f5d12;
    --gold-light: #8a7618;
    --paper: #ffffff;
  }
  html, body {
    margin: 0;
    padding: 0;
    width: 1200px;
    height: 685px;
    overflow: hidden;
    background: var(--paper);
  }
  .card {
    position: relative;
    width: 1200px;
    height: 685px;
    background: var(--paper);
    font-family: "Lato", sans-serif;
    color: var(--ink);
  }
  .card__waves {
    position: absolute;
    inset: 0;
    width: 1200px;
    height: 685px;
  }
  .brand {
    position: absolute;
    left: 800px;
    top: 150px;
    width: 310px;
    text-align: center;
  }
  .brand__name {
    font-family: "Lato", sans-serif;
    font-weight: 700;
    font-size: 34px;
    letter-spacing: 1px;
    color: var(--gold-light);
  }
  .contact {
    position: absolute;
    left: 67px;
    top: 355px;
  }
  .contact__name {
    margin: 0 0 38px;
    font-weight: 700;
    font-size: 58px;
    letter-spacing: 1px;
    text-transform: uppercase;
    line-height: 1;
  }
  .contact__row {
    display: flex;
    align-items: center;
    gap: 22px;
    font-size: 46px;
    line-height: 1;
    margin-bottom: 30px;
    letter-spacing: 1px;
  }
  .contact__icon {
    width: 40px;
    height: 40px;
    flex: none;
  }
</style>
</head>
<body>
  <div class="card">
    <svg class="card__waves" viewBox="0 0 1200 685" aria-hidden="true">
      <path class="wave-gold" fill="var(--gold)"
        d="M0,0 H1200 V545 C1130,570 1020,580 900,555 C760,520 620,440 480,350 C340,270 170,260 0,320 Z"/>
      <path class="wave-white" fill="var(--paper)"
        d="M0,0 H1200 V520 C1120,540 1010,548 900,520 C760,480 620,380 470,295 C330,215 160,205 0,240 Z"/>
      <path class="wave-black" fill="var(--black)"
        d="M0,0 H1200 V505 C1120,525 1000,535 900,500 C760,450 620,310 470,220 C330,140 150,135 0,165 Z"/>
    </svg>

    <div class="brand">
      <span class="brand__name">Copperleaf Dukes</span>
    </div>

    <div class="contact">
      <h1 class="contact__name">Rek Tamuno</h1>
      <div class="contact__row">
        <svg class="contact__icon" viewBox="0 0 24 24" aria-hidden="true" fill="none" stroke="var(--gold)" stroke-width="1.8" stroke-linejoin="round">
          <path d="M5 3h4l2 5-2.5 1.5a11 11 0 0 0 6 6L16 13l5 2v4a2 2 0 0 1-2 2A16 16 0 0 1 3 5a2 2 0 0 1 2-2z"/>
        </svg>
        <span class="contact__text">021 04731952</span>
      </div>
      <div class="contact__row">
        <svg class="contact__icon" viewBox="0 0 24 24" aria-hidden="true" fill="none" stroke="var(--gold)" stroke-width="1.6">
          <circle cx="12" cy="12" r="9"/>
          <ellipse cx="12" cy="12" rx="4" ry="9"/>
          <path d="M3 12h18M4.5 7.5h15M4.5 16.5h15"/>
        </svg>
        <span class="contact__text">www.copperleafdukes.co.nz</span>
      </div>
    </div>
  </div>
</body>
</html>
```